Tarvel Ridge LLC

Need Professional Business cards for New Investment Fund

Target Market(s)

High Quality investors

Industry/Entity Type

Financial

Contact Information for Business Card

Phone Number +1 555 284 6193
Name Pavel Orlinsky
Title Fund Manager
email po@FundTarvel.example
Website www.FundTarvel.example

Colors

Designer to choose colors to be used in the design.

Requirements
Must have
• Must have our Logo and all of the above. Must be made so lettering and loge can be raised

```html
<!DOCTYPE html>
<html lang="en">
<head>
<meta charset="utf-8">
<title>Tarvel Ridge LLC — Business Card</title>
<link rel="stylesheet" href="https://fonts.googleapis.com/css2?family=Lato:wght@400;700&display=swap">
<style>
  :root {
    --green: #1fe608;
    --slate: #414a40;
    --paper: #f3f3f3;
    --ink: #3d3d3d;
    --rule: #bdbdbd;
    --backdrop: #e4e4e4;
  }
  * { box-sizing: border-box; margin: 0; padding: 0; }
  html, body { width: 1200px; height: 1015px; overflow: hidden; }
  body {
    background: var(--backdrop);
    font-family: "Lato", Arial, sans-serif;
    display: flex;
    flex-direction: column;
    align-items: center;
    justify-content: center;
    gap: 56px;
  }
  .card {
    position: relative;
    width: 760px;
    height: 434px;
    overflow: hidden;
    box-shadow: 0 10px 28px rgba(0,0,0,.25);
  }

  /* Back side */
  .card--back { background: var(--slate); }
  .card--back .split { position: absolute; inset: 0; width: 100%; height: 100%; }
  .back-name {
    position: absolute;
    left: 0; right: 0; top: 50%;
    transform: translateY(-50%);
    text-align: center;
    color: #ffffff;
    font-weight: 700;
    font-size: 64px;
    letter-spacing: 2px;
  }

  /* Front side */
  .card--front { background: var(--paper); }
  .brand {
    position: absolute;
    left: 70px; top: 180px;
    display: flex; align-items: center; gap: 14px;
  }
  .brand-mark { width: 22px; height: 22px; background: var(--green); }
  .brand-name { color: var(--slate); font-weight: 700; font-size: 34px; letter-spacing: 1px; }
  .divider {
    position: absolute;
    left: 372px; top: 90px;
    width: 1px; height: 205px;
    background: var(--rule);
  }
  .details { position: absolute; left: 405px; top: 108px; color: var(--ink); }
  .person-name { font-weight: 700; font-size: 27px; letter-spacing: .5px; color: var(--slate); }
  .person-name .first { color: var(--green); }
  .person-title { font-size: 19px; margin-top: 2px; }
  .contacts { list-style: none; margin-top: 30px; }
  .contacts li { display: flex; align-items: center; gap: 10px; font-size: 19px; line-height: 28px; }
  .contacts svg { width: 14px; height: 14px; flex: none; }
  .band-green {
    position: absolute; left: 0; bottom: 0;
    width: 478px; height: 26px;
    background: var(--green);
  }
  .band-slate {
    position: absolute; right: 0; bottom: 0;
    width: 276px; height: 44px;
    background: var(--slate);
  }
</style>
</head>
<body>

  <section class="card card--back" aria-label="Card back">
    <svg class="split" viewBox="0 0 760 434" preserveAspectRatio="none" aria-hidden="true">
      <polygon points="0,0 330,0 420,434 0,434" fill="var(--green)"/>
    </svg>
    <div class="back-name">Tarvel Ridge</div>
  </section>

  <section class="card card--front" aria-label="Card front">
    <div class="brand">
      <span class="brand-mark"></span>
      <span class="brand-name">Tarvel Ridge</span>
    </div>
    <div class="divider"></div>
    <div class="details">
      <p class="person-name"><span class="first">PAVEL</span> ORLINSKY</p>
      <p class="person-title">Fund Manager</p>
      <ul class="contacts">
        <li>
          <svg viewBox="0 0 14 14" aria-hidden="true"><path fill="var(--green)" d="M3 1l2 3-1.5 1.5a7 7 0 0 0 5 5L10 9l3 2-1.5 2.5C6 13 1 8 .5 2.5z"/></svg>
          +1 555 284 6193
        </li>
        <li>
          <svg viewBox="0 0 14 14" aria-hidden="true"><rect x="0.5" y="2.5" width="13" height="9" fill="var(--green)"/><path d="M1 3l6 5 6-5" stroke="#fff" stroke-width="1.2" fill="none"/></svg>
          po@FundTarvel.example
        </li>
        <li>
          <svg viewBox="0 0 14 14" aria-hidden="true"><circle cx="7" cy="7" r="6.5" fill="var(--green)"/><path d="M1 7h12M7 1c-3 3-3 9 0 12M7 1c3 3 3 9 0 12" stroke="#fff" stroke-width="1" fill="none"/></svg>
          www.FundTarvel.example
        </li>
      </ul>
    </div>
    <div class="band-green"></div>
    <div class="band-slate"></div>
  </section>

</body>
</html>
```